New Business Card/Website Logo

We need a business card design for a new company based in Sydney. The company focuses mainly in construction in the field of form work and concreting. Attached is the logo being used already which can be used as a base for a new design, the current one is simply too bland and we are looking to spruce it up so it stands out and looks nicer. The logo would also be used on the website which is currently under construction. The attached image has the name, mobile and also the license number which needs to be there. The current email address on there can be removed and can be replaced with the website http://www.pillarvane.com.au, thanks!
Updates

Target Market(s)

Construction industry. Focusing on form work and concreting

Industry/Entity Type

Construction

Requirements
Must have
• License # on card along with website http://www.pillarvane.com.au and mobile phone number
Nice to have
• You have freedom with the design. The current design was a mock up done quite quickly. Please just keep in mind the target audience - construction, thanks.
Should not have
• the breezepost email address can be removed(refer picture) and replaced somewhere on the design with the website http://www.pillarvane.com.au

```html
<!DOCTYPE html>
<html lang="en">
<head>
<meta charset="utf-8">
<title>PillarVane Business Card</title>
<link rel="stylesheet" href="https://fonts.googleapis.com/css2?family=Arimo:ital,wght@0,400;0,700;1,400&display=swap">
<style>
  :root {
    --backdrop: #1c3a14;
    --card: #050505;
    --ink: #f4f4f4;
    --accent: #5f9e4a;
  }
  * { margin: 0; padding: 0; box-sizing: border-box; }
  html, body {
    width: 1200px;
    height: 900px;
    overflow: hidden;
    background: var(--backdrop);
    font-family: "Arimo", Arial, sans-serif;
  }
  .business-card {
    position: absolute;
    left: 150px;
    top: 175px;
    width: 900px;
    height: 550px;
    background: var(--card);
    border-radius: 4px;
    box-shadow: 0 18px 40px rgba(0, 0, 0, 0.45);
    color: var(--ink);
  }
  .brand {
    position: absolute;
    left: 60px;
    top: 50px;
    display: flex;
    align-items: center;
    gap: 18px;
  }
  .brand-mark {
    width: 82px;
    height: 64px;
    background: var(--accent);
    border-radius: 6px;
  }
  .brand-name {
    font-size: 31px;
    font-weight: 400;
    letter-spacing: 1px;
    line-height: 1;
  }
  .brand-url {
    font-size: 19px;
    margin-top: 6px;
  }
  .contact {
    position: absolute;
    right: 70px;
    top: 160px;
    text-align: right;
  }
  .person-name {
    font-size: 40px;
    font-weight: 400;
  }
  .person-name .given { font-weight: 700; }
  .phone {
    display: flex;
    justify-content: flex-end;
    align-items: center;
    gap: 12px;
    font-size: 23px;
    margin-top: 10px;
  }
  .phone-icon { width: 24px; height: 24px; }
  .licence {
    position: absolute;
    left: 55px;
    bottom: 60px;
    font-size: 25px;
    font-style: italic;
  }
</style>
</head>
<body>
  <main class="business-card">
    <header class="brand">
      <div class="brand-mark"></div>
      <div class="brand-text">
        <div class="brand-name">PILLARVANE</div>
        <div class="brand-url">www.pillarvane.com.au</div>
      </div>
    </header>

    <section class="contact">
      <div class="person-name"><span class="given">Mateo</span> Alvarez</div>
      <div class="phone">
        <span>0412 555 190</span>
        <svg class="phone-icon" viewBox="0 0 24 24" aria-hidden="true">
          <circle cx="12" cy="12" r="12" fill="var(--accent)"/>
          <path d="M8.2 6.2c.4-.3.9-.3 1.2.1l1.3 1.8c.3.4.2.9-.1 1.2l-.8.7c.5 1.3 1.6 2.6 3 3.3l.8-.7c.3-.3.8-.3 1.2 0l1.8 1.3c.4.3.4.9.1 1.2l-1 1.1c-.5.5-1.3.7-2 .4-3-1.2-5.4-3.6-6.5-6.6-.3-.7-.1-1.5.4-2z" fill="var(--card)"/>
        </svg>
      </div>
    </section>

    <footer class="licence">Licence # 348215c</footer>
  </main>
</body>
</html>
```